IT services company requires Letterhead design

We need a professional letterhead designed to be used for general correspondence with customers, quotes, invoices etc. We are a new IT services company specialising in computer servicing and repairs and mobile and tablet repairs. Attached are templates that my printing company have supplied, my logos, an interpretation of our website for you to get a feel of the company. Details to be included on the letterhead are

Company Number – 4830517
VAT Number - 581736294
Registered Address – 14-16 Brambury Lane, London, E9 3PL

Phone – 01843 572236
Email – sales@quorvant.com
Web – www.quorvant.com

I would prefer for the top of the letterhead to just have the company logo on a white background and the rest of the details on the bottom of the letterhead but I am open to design ideas.

Thanks

```html
<!DOCTYPE html>
<html lang="en">
<head>
<meta charset="utf-8">
<title>Quorvant Letterhead</title>
<link rel="stylesheet" href="https://fonts.googleapis.com/css2?family=Roboto+Slab:wght@700;800&display=swap">
<style>
  :root {
    --ink: #0d1520;
    --cyan: #12f4fb;
    --paper: #ffffff;
    --rule: #9a9a9a;
    --ghost: #ececec;
    --text: #1a1a1a;
  }
  * { box-sizing: border-box; margin: 0; padding: 0; }
  html, body { width: 848px; height: 1200px; overflow: hidden; background: var(--paper); }
  .letterhead {
    position: relative;
    width: 848px;
    height: 1200px;
    overflow: hidden;
    background: var(--paper);
    font-family: "Roboto Slab", Georgia, serif;
  }

  /* Left block strip */
  .side-strip { position: absolute; left: 0; top: 0; width: 48px; }
  .side-strip .block { position: absolute; left: 0; width: 48px; height: 71px; }
  .block--cyan { background: var(--cyan); }
  .block--ink { background: var(--ink); }

  /* Brand header */
  .brand-tab { position: absolute; left: 51px; top: 0; width: 149px; height: 145px; }
  .brand-tab svg { position: absolute; inset: 0; }
  .brand-name {
    position: absolute; left: 22px; top: 50px;
    display: flex; align-items: center; gap: 6px;
    color: var(--paper); font-weight: 800; font-size: 19px; letter-spacing: 0.2px;
    white-space: nowrap;
  }
  .brand-square { width: 9px; height: 9px; background: var(--cyan); }

  /* Registration details */
  .registration {
    position: absolute; left: 598px; top: 20px;
    border-left: 1.5px solid var(--rule);
    padding-left: 16px; height: 94px;
  }
  .registration li {
    list-style: none; position: relative;
    font-size: 11.5px; font-weight: 700; color: var(--text);
    line-height: 25px; padding-left: 22px; white-space: nowrap;
  }
  .registration .icon { position: absolute; left: 0; top: 6px; width: 12px; height: 13px; }

  /* Faint name mark */
  .ghost-mark {
    position: absolute; left: 48px; right: 0; top: 600px;
    text-align: center;
    font-size: 120px; font-weight: 800; color: var(--ghost);
    letter-spacing: -2px; white-space: nowrap;
  }

  /* Footer band */
  .footer-band { position: absolute; left: 0; top: 1054px; width: 292px; height: 146px; }
  .footer-band svg { position: absolute; inset: 0; }
  .contact-list { position: absolute; left: 50px; top: 40px; }
  .contact-list li {
    list-style: none; position: relative;
    color: var(--paper); font-size: 11.5px; font-weight: 700;
    line-height: 24.5px; padding-left: 18px; white-space: nowrap;
  }
  .contact-list .icon { position: absolute; left: 0; top: 6px; width: 12px; height: 12px; }
</style>
</head>
<body>
<div class="letterhead">

  <div class="side-strip">
    <div class="block block--cyan" style="top:0"></div>
    <div class="block block--ink" style="top:75px"></div>
    <div class="block block--cyan" style="top:150px"></div>
    <div class="block block--ink" style="top:225px"></div>
    <div class="block block--cyan" style="top:300px"></div>
    <div class="block block--ink" style="top:375px"></div>
    <div class="block block--cyan" style="top:450px"></div>
    <div class="block block--ink" style="top:525px"></div>
    <div class="block block--cyan" style="top:600px"></div>
    <div class="block block--ink" style="top:675px"></div>
    <div class="block block--cyan" style="top:750px"></div>
    <div class="block block--ink" style="top:825px"></div>
    <div class="block block--cyan" style="top:900px"></div>
    <div class="block block--ink" style="top:975px"></div>
  </div>

  <header class="brand-tab">
    <svg viewBox="0 0 149 145" width="149" height="145">
      <polygon points="0,0 149,0 149,82 60,145 0,145" fill="var(--ink)"/>
      <polygon points="100,135 139,107 139,135" fill="var(--ink)"/>
    </svg>
    <div class="brand-name"><span class="brand-square"></span>Quorvant</div>
  </header>

  <ul class="registration">
    <li>
      <svg class="icon" viewBox="0 0 12 13"><circle cx="7" cy="3" r="2.5" fill="var(--text)"/><rect x="2" y="6" width="6" height="6" rx="1" fill="var(--text)"/></svg>
      Company Number – 4830517
    </li>
    <li>VAT Number - 581736294</li>
    <li>
      <svg class="icon" viewBox="0 0 12 13"><path d="M6 12 C2 7 2 5.5 2 4.5 A4 4 0 0 1 10 4.5 C10 5.5 10 7 6 12Z" fill="none" stroke="var(--text)" stroke-width="1.6"/></svg>
      Address – 14-16 Brambury Lane,<br>London, E9 3PL
    </li>
  </ul>

  <div class="ghost-mark" aria-hidden="true">Quorvant</div>

  <footer class="footer-band">
    <svg viewBox="0 0 292 146" width="292" height="146">
      <polygon points="0,0 200,0 292,146 0,146" fill="var(--ink)"/>
    </svg>
    <ul class="contact-list">
      <li>
        <svg class="icon" viewBox="0 0 12 12"><path d="M2 1 L4.5 1 L5.5 4 L4 5 C5 7 6 8 8 9 L9 7.5 L11.5 8.5 L11.5 11 C6 11 1 6 1 1Z" fill="var(--paper)"/></svg>
        Phone – 01843 572236
      </li>
      <li>
        <svg class="icon" viewBox="0 0 12 12"><rect x="1" y="3" width="10" height="7" fill="none" stroke="var(--paper)" stroke-width="1.3"/><path d="M1 3 L6 7 L11 3" fill="none" stroke="var(--paper)" stroke-width="1.3"/></svg>
        Email – sales@quorvant.com
      </li>
      <li>
        <svg class="icon" viewBox="0 0 12 12"><circle cx="6" cy="6" r="5" fill="none" stroke="var(--paper)" stroke-width="1.2"/><ellipse cx="6" cy="6" rx="2.2" ry="5" fill="none" stroke="var(--paper)" stroke-width="1"/><path d="M1 6 H11" stroke="var(--paper)" stroke-width="1"/></svg>
        Web – www.quorvant.com
      </li>
    </ul>
  </footer>

</div>
</body>
</html>
```